We are the world's leading center for transgender surgery and have multiple locations.

We want a unique and dynamic business card that wows potential patients and referral sources (physicians, previous patients, etc). We are open to inventive designs, card shape, additional design on the back of the card, etc.

We are a surgical practice in a competitive environment and want to stand out as the leader in transgender surgery. We have multiple surgeons with unique talents who are impeccably trained with extensive experience. We are dedicated to our patients and their needs. We want the card to stand out and impress them. We want it to be suitable to all of the surgeons as well as our staff.

Our practice started as a small practice in San Francisco, CA and now has an additional location in Austin Texas (as well as another city to be announced later). Our practice has plastic surgeons, reconstructive urologists, general surgeons and gynecologists.

We continue to boast some of the lowest published phalloplasty complication rates in the world and our San Francisco microsurgeons that we have been working with for more than a year and a half have 0 microvascular take backs and 0 flap failures. Between our two centers in San Francisco, California and Austin, Texas, we perform 5-6 phalloplasties per week, making us one of the largest volume centers in the world.

Target Market(s)

Potential Transgender patients (all genders) and referring physicians

Industry/Entity Type

Surgeon

Contact Information for Business Card

Here is an example of one of our physicians:

Daniel R. Ostrow, MD
Reconstructive Urology for the Transgender Community
Diplomate, National Council of Renal Medicine with subspecialty certification in FPS and Reconstructive Surgery

318 Lady Harriet Moore Ave
Suite 7
Greenbrae, CA 94817

phone 415-738-1942
fax 415-582-1947

Font styles to use
Sans Serif

Requirements
Must have
• Must have a unique look, but tasteful.
Nice to have
• ?
Should not have
• ?

```html
<!DOCTYPE html>
<html lang="en">
<head>
<meta charset="utf-8">
<title>Heron Institute – Business Card</title>
<link rel="stylesheet" href="https://fonts.googleapis.com/css2?family=Open+Sans:wght@400;600;700&display=swap">
<style>
  :root {
    --stage: #a9a9a9;
    --card-black: #141414;
    --navy: #27306e;
    --navy-deep: #1e2660;
    --magenta: #b01f7c;
    --magenta-dark: #7e1559;
    --periwinkle: #7f93d6;
    --white: #ffffff;
    --text-soft: #e8e8ee;
  }
  * { box-sizing: border-box; margin: 0; padding: 0; }
  html, body {
    width: 1200px; height: 900px; overflow: hidden;
    background: radial-gradient(circle at 50% 45%, #d2d2d2 0%, var(--stage) 80%);
    font-family: "Open Sans", Arial, sans-serif;
  }
  .stage {
    width: 1200px; height: 900px;
    display: flex; align-items: center; justify-content: center; gap: 40px;
  }
  .card {
    position: relative;
    width: 560px; height: 320px;
    border-radius: 20px;
    overflow: hidden;
    background: var(--card-black);
    box-shadow: 0 10px 24px rgba(0,0,0,.35);
  }
  .card__art { position: absolute; inset: 0; }

  /* front */
  .front__name {
    position: absolute; left: 36px; top: 26px;
    color: var(--text-soft); font-size: 21px; font-weight: 400;
    letter-spacing: .5px; text-transform: uppercase; white-space: nowrap;
  }
  .front__name .degree { color: var(--magenta); font-size: 13px; text-transform: uppercase; margin-left: 4px; }
  .front__credentials {
    position: absolute; left: 36px; top: 80px;
    color: var(--white); font-size: 10px; line-height: 14px; white-space: nowrap;
  }
  .brand {
    position: absolute; left: 28px; top: 200px;
    display: flex; align-items: center; gap: 8px;
  }
  .brand__dot { width: 26px; height: 26px; border-radius: 50%; background: var(--white); }
  .brand__name { color: var(--white); font-size: 16px; font-weight: 700; letter-spacing: .5px; text-transform: uppercase; }
  .brand__tag {
    position: absolute; left: 62px; top: 229px;
    color: var(--text-soft); font-size: 5.5px; letter-spacing: .6px; text-transform: uppercase;
  }
  .contact {
    position: absolute; right: 26px; top: 196px;
    list-style: none; text-align: right;
    color: var(--white); font-size: 13px; line-height: 20px;
  }
  .contact li { display: flex; justify-content: flex-end; align-items: flex-start; gap: 10px; }
  .contact__icon {
    flex: none; width: 14px; height: 14px; margin-top: 3px;
    border-radius: 50%; background: var(--magenta);
    display: flex; align-items: center; justify-content: center;
  }
  .contact__icon--blank { background: transparent; }

  /* back */
  .back__brand {
    position: absolute; right: 34px; bottom: 64px; text-align: right;
  }
  .back__name { color: var(--magenta); font-size: 32px; font-weight: 700; letter-spacing: .5px; text-transform: uppercase; line-height: 1; }
  .back__tag { color: var(--periwinkle); font-size: 8px; font-weight: 600; letter-spacing: 1px; text-transform: uppercase; margin-top: 5px; }
</style>
</head>
<body>
<main class="stage">

  <section class="card card--front" aria-label="Business card, front">
    <svg class="card__art" width="560" height="320" viewBox="0 0 560 320" aria-hidden="true">
      <polygon class="navy-field" points="0,158 372,158 388,172 560,172 560,320 0,320" fill="var(--navy)"/>
      <rect class="ribbon" x="0" y="66" width="420" height="84" fill="var(--magenta)"/>
      <polygon class="ribbon-fold" points="388,150 420,150 420,166" fill="var(--magenta-dark)"/>
    </svg>

    <h1 class="front__name">Daniel R. Ostrow,<span class="degree">MD</span></h1>
    <p class="front__credentials">
      Reconstructive Urology for the Transgender Community<br>
      Diplomate,<br>
      National Council of Renal Medicine with subspecialty certification in<br>
      FPS and Reconstructive Surgery
    </p>

    <div class="brand">
      <span class="brand__dot"></span>
      <span class="brand__name">Heron Institute</span>
    </div>
    <span class="brand__tag">For Transgender Surgery</span>

    <ul class="contact">
      <li>000 000 0000
        <span class="contact__icon"><svg width="8" height="8" viewBox="0 0 8 8"><path d="M1.5 1h1.5l.6 1.6-.9.7a4 4 0 0 0 2 2l.7-.9L7 5v1.5A.6.6 0 0 1 6.4 7 5.6 5.6 0 0 1 1 1.6.6.6 0 0 1 1.5 1z" fill="#fff"/></svg></span></li>
      <li>youremail@xyz.com
        <span class="contact__icon"><svg width="8" height="8" viewBox="0 0 8 8"><rect x=".8" y="1.8" width="6.4" height="4.4" fill="none" stroke="#fff" stroke-width=".9"/><path d="M.8 2l3.2 2.3L7.2 2" fill="none" stroke="#fff" stroke-width=".9"/></svg></span></li>
      <li>www.yourwebsite.com
        <span class="contact__icon"><svg width="8" height="8" viewBox="0 0 8 8"><circle cx="4" cy="4" r="3" fill="none" stroke="#fff" stroke-width=".8"/><path d="M1 4h6M4 1c-1.6 2-1.6 4 0 6M4 1c1.6 2 1.6 4 0 6" fill="none" stroke="#fff" stroke-width=".6"/></svg></span></li>
      <li>0000, Anywhere, Somewhere<span class="contact__icon contact__icon--blank"></span></li>
      <li>City, ST 0000<span class="contact__icon contact__icon--blank"></span></li>
    </ul>
  </section>

  <section class="card card--back" aria-label="Business card, back">
    <div class="back__brand">
      <div class="back__name">Heron Institute</div>
      <div class="back__tag">For Transgender Surgery</div>
    </div>
  </section>

</main>
</body>
</html>
```